Blu-ray disc cover

Cover for a video calibration product;

The Brand name is MORVANTEQO (the font used is all caps Gotham Black)
The product name is HOLLOW DAWNRISE (the font is also Gotham black).

A few style guides-
The background should be black, although some rays as with the QVR are ok.

The name HOLLOW DAWNRISE should not be turned into a logo. It should literally be the gotham font with the RGB color value GREEN colour: R=154, G=202, B=60

I included a mockup, but I don't like it, but i do want something with some pizzaz within the very strict guidelines

Industry/Entity Type

Product

Font styles to use
Sans Serif

Colors
9bcb3c

Requirements
Must have
• Almost 99% sure it should show a TV screen of some sort, or abstract of one.
Nice to have
• Ideally, there would be some feeling of dynamism and of different things you'd watch on TV (like soccer, racing, nature, action), but in some sort of abstract way.
Should not have
• Shouldn't have any elements that represent film or photography. We clearly want this to be a TV product.

```html
<!DOCTYPE html>
<html lang="en">
<head>
<meta charset="utf-8">
<title>Hollow Dawnrise — Morvanteqo</title>
<link rel="stylesheet" href="https://fonts.googleapis.com/css2?family=Montserrat:wght@400;800;900&display=swap">
<style>
  :root {
    --bg-deep: #1e1c1e;
    --bg-glow: #5a585a;
    --brand-green: #9bcb3c;
    --green-shade: #1d5a30;
    --text-light: #e6e6e6;
    --bezel: #0b0b0c;
    --bezel-edge: #2c2c2e;
    --screen-off: #141416;
    --accent-purple: #6a2c8e;
    --tagline: #d9d9d9;
  }
  html, body {
    margin: 0;
    padding: 0;
    width: 1020px;
    height: 1200px;
    overflow: hidden;
    background: var(--bg-deep);
  }
  .cover {
    position: relative;
    width: 1020px;
    height: 1200px;
    overflow: hidden;
    background:
      radial-gradient(ellipse 520px 420px at 510px 330px, var(--bg-glow) 0%, #3a383a 40%, var(--bg-deep) 100%);
    font-family: "Montserrat", sans-serif;
  }
  .cover-art {
    position: absolute;
    inset: 0;
  }
  .product-title {
    font-family: "Montserrat", sans-serif;
    font-weight: 900;
    font-size: 95px;
  }
  .tagline {
    font-family: "Montserrat", sans-serif;
    font-weight: 400;
    font-size: 25px;
    letter-spacing: 1.6px;
    fill: var(--tagline);
  }
  .control-label {
    font-family: "Montserrat", sans-serif;
    font-weight: 400;
    font-size: 5px;
    fill: #8a8a8a;
  }
  .brand-name {
    font-family: "Montserrat", sans-serif;
    font-weight: 800;
    font-size: 46px;
    fill: #ffffff;
  }
</style>
</head>
<body>
<main class="cover">
  <svg class="cover-art" width="1020" height="1200" viewBox="0 0 1020 1200" xmlns="http://www.w3.org/2000/svg">
    <defs>
      <linearGradient id="scene-fill" x1="0" y1="0" x2="0" y2="1">
        <stop offset="0" stop-color="#7ea8d6"/>
        <stop offset="0.35" stop-color="#c9d6e4"/>
        <stop offset="0.55" stop-color="#b2582a"/>
        <stop offset="0.8" stop-color="#5c6b3a"/>
        <stop offset="1" stop-color="#2e3a24"/>
      </linearGradient>
      <linearGradient id="stand-fill" x1="0" y1="0" x2="0" y2="1">
        <stop offset="0" stop-color="#2a2a2c"/>
        <stop offset="1" stop-color="#050505"/>
      </linearGradient>
    </defs>

    <!-- Product title -->
    <g class="title-block">
      <text class="product-title" x="55" y="172" fill="var(--green-shade)" textLength="925" lengthAdjust="spacingAndGlyphs">HOLLOW DAWNRISE</text>
      <text class="product-title" x="58" y="177" fill="var(--brand-green)" textLength="925" lengthAdjust="spacingAndGlyphs">HOLLOW DAWNRISE</text>
      <text class="tagline" x="976" y="222" text-anchor="end">Get the Whole Picture From Your Television</text>
    </g>

    <!-- Floor block -->
    <rect class="floor-block" x="129" y="1064" width="775" height="136" fill="#1a191a"/>

    <!-- Television -->
    <g class="television">
      <rect class="tv-bezel" x="132" y="364" width="774" height="483" rx="4" fill="var(--bezel)" stroke="var(--bezel-edge)" stroke-width="1.5"/>
      <rect class="tv-screen" x="155" y="388" width="731" height="410" fill="var(--screen-off)" stroke="#3a3a3c" stroke-width="1"/>
      <rect class="tv-picture" x="256" y="391" width="537" height="403" fill="url(#scene-fill)" role="img" aria-label="Landscape photograph of a red sandstone butte under a blue sky with clouds, with a circular calibrated area highlighting richer colour"/>
      <circle class="calibration-lens" cx="520" cy="585" r="190" fill="none" stroke="rgba(255,255,255,0.25)" stroke-width="1.5"/>
      <g class="tv-controls">
        <text class="control-label" x="686" y="831">INPUT</text>
        <text class="control-label" x="707" y="831">MENU</text>
        <text class="control-label" x="728" y="831">OK</text>
        <text class="control-label" x="742" y="831">▼ VOL ▲</text>
        <text class="control-label" x="788" y="831">▼ PR ▲</text>
        <text class="control-label" x="826" y="831">QUIT</text>
      </g>
      <circle class="power-button" cx="191" cy="827" r="3" fill="none" stroke="#555" stroke-width="0.8"/>
      <path class="tv-neck" d="M504 847 L537 847 L542 906 L499 906 Z" fill="url(#stand-fill)"/>
      <ellipse class="tv-base" cx="518" cy="921" rx="185" ry="24" fill="url(#stand-fill)" stroke="#3a3a3c" stroke-width="1"/>
    </g>

    <!-- Brand -->
    <g class="brand-lockup">
      <circle class="brand-dot" cx="638" cy="1126" r="33" fill="var(--accent-purple)"/>
      <text class="brand-name" x="684" y="1143" textLength="302" lengthAdjust="spacingAndGlyphs">MORVANTEQO</text>
    </g>
  </svg>
</main>
</body>
</html>
```